Pictures required on web page

I would like change three existing pictures on my new website.

The site can be found here:
http://mossbottleroom.kestrelweb.com.au/

The three pictures to be changed are on the home page:
Purchase- Mixed Packs
Wine Club - Let Us Choose
Education- Wine Courses

I would like somthing stylish, classic and understated that fits in with the theme and feel of the site. I know stylish is a subjective thing. At the moment, the current picture makes the text difficult to read on a destop. Plus I don't think they are a perfect fit for our website anyway. I've attached a photo of our wine course room and also me in the store. Please, don't feel as though you have to use these pictures, but they're there if you want them. However I'm open to completely different photos/graphics to be used.

```html
<!DOCTYPE html>
<html lang="en">
<head>
<meta charset="utf-8">
<title>Mossbottle – Small winery specialist</title>
<link rel="stylesheet" href="https://fonts.googleapis.com/css2?family=Roboto+Slab:wght@300;700&family=Roboto:wght@400&family=Noto+Serif:wght@400;700&display=swap">
<style>
  :root {
    --header-top: #2d3f60;
    --header-bottom: #1d2a45;
    --nav-bar: #151d2c;
    --white: #ffffff;
    --icon: #c9d2e3;
    --search-bg: #33476b;
    --search-border: #6b7fa3;
    --divider: #3e5174;
    --ribbon-red: #b3474a;
    --ribbon-red-fold: #7d2a2c;
    --ribbon-navy: #1e2a44;
    --ribbon-navy-fold: #1f5fa8;
    --page: #ffffff;
  }
  * { box-sizing: border-box; margin: 0; padding: 0; }
  html, body { width: 1200px; height: 679px; overflow: hidden; background: var(--page); }
  body { position: relative; font-family: "Roboto", Arial, sans-serif; }

  .site-header {
    position: absolute; left: 0; top: 0; width: 1200px; height: 100px;
    background: linear-gradient(var(--header-top), var(--header-bottom));
    border-top: 1px solid #5a6c8c;
  }
  .brand { position: absolute; left: 128px; top: 18px; color: var(--white); }
  .brand-name { font-family: "Roboto Slab", Georgia, serif; font-weight: 700; font-size: 35px; line-height: 40px; letter-spacing: -0.3px; }
  .brand-tagline { font-family: "Roboto Slab", Georgia, serif; font-weight: 300; font-size: 16.5px; line-height: 20px; }

  .search {
    position: absolute; left: 390px; top: 33px; width: 270px; height: 32px;
    background: var(--search-bg); border: 1px solid var(--search-border); border-radius: 3px;
    color: #aab6cc; font-size: 14px; line-height: 30px; padding-left: 12px;
  }
  .search svg { position: absolute; right: 8px; top: 4px; }

  .utility-nav { position: absolute; left: 687px; top: 28px; display: flex; }
  .utility-link {
    width: 74.5px; height: 40px; text-align: center; color: var(--white);
    font-size: 11px; border-left: 1px solid var(--divider);
  }
  .utility-link:first-child { border-left: none; }
  .utility-link svg { display: block; margin: 3px auto 7px; height: 16px; }

  .category-bar {
    position: absolute; left: 0; top: 100px; width: 1200px; height: 44px;
    background: var(--nav-bar);
  }
  .categories { position: absolute; left: 129px; top: 0; display: flex; gap: 27px; }
  .categories span { color: var(--white); font-size: 16.5px; line-height: 44px; }
  .cart { position: absolute; left: 909px; top: 12px; color: var(--white); font-size: 12.5px; display: flex; align-items: center; gap: 8px; }

  .content { position: absolute; left: 77px; top: 144px; width: 1027px; height: 535px; background: var(--page); }

  .feature { position: absolute; top: 164px; width: 305px; height: 417px; }
  .feature-photo { position: absolute; inset: 0; }
  .feature-education .feature-photo {
    background:
      radial-gradient(ellipse 55% 35% at 62% 24%, rgba(255,214,120,0.95), rgba(255,170,60,0) 70%),
      linear-gradient(180deg, #9c5a1c 0%, #d48a2c 22%, #b8782a 45%, #6b6a26 68%, #3c4418 100%);
  }
  .feature-club .feature-photo {
    background: linear-gradient(180deg, #f4e2ec 0%, #e6cde0 28%, #c9b4d6 44%, #4a52b4 56%, #2b36a0 78%, #1b2488 100%);
  }
  .feature-packs .feature-photo {
    background: linear-gradient(180deg, #cfcfb8 0%, #a7a25a 16%, #8c8a3c 38%, #9a7a52 58%, #c2a06c 78%, #b8a27e 100%);
  }

  .corner-ribbon { position: absolute; left: -20px; top: -20px; overflow: visible; }
  .corner-label {
    position: absolute; left: -42px; top: 30px; width: 150px; height: 28px;
    transform: rotate(-45deg); color: var(--white);
    font-family: "Noto Serif", Georgia, serif; font-size: 17px; line-height: 28px; text-align: center;
  }

  .title-banner { position: absolute; left: 102px; top: 300px; width: 222px; height: 44px; }
  .title-banner svg { position: absolute; left: 0; top: 0; }
  .title-banner span {
    position: absolute; left: 18px; top: 0; width: 204px; line-height: 34px; text-align: center;
    color: var(--white); font-family: "Noto Serif", Georgia, serif; font-size: 23px;
    text-shadow: 0 1px 2px rgba(0,0,0,0.35);
  }

  .read-more {
    position: absolute; right: 16px; bottom: 15px; height: 24px; padding: 0 9px;
    border: 1px solid rgba(255,255,255,0.85); color: var(--white);
    font-family: "Noto Serif", Georgia, serif; font-weight: 700; font-size: 10px; line-height: 22px;
  }

  .product { position: absolute; top: 613px; height: 66px; }
  .bottle { background: linear-gradient(#1d1a18, #2b2420); border-radius: 18px 18px 0 0; }
</style>
</head>
<body>
  <header class="site-header">
    <div class="brand">
      <div class="brand-name">Mossbottle</div>
      <div class="brand-tagline">Small winery specialist.</div>
    </div>
    <div class="search">Search the Cellars
      <svg width="22" height="22" viewBox="0 0 22 22" fill="none" stroke="#ffffff" stroke-width="2"><circle cx="9" cy="9" r="6.5"/><line x1="14" y1="14" x2="20" y2="20"/></svg>
    </div>
    <nav class="utility-nav">
      <div class="utility-link">
        <svg width="16" height="14" viewBox="0 0 16 14" fill="#c9d2e3"><path d="M8 0 L16 7 H13.5 V14 H10 V9.5 H6 V14 H2.5 V7 H0 Z"/></svg>HOME</div>
      <div class="utility-link">
        <svg width="20" height="14" viewBox="0 0 20 14" fill="#c9d2e3"><circle cx="10" cy="3.5" r="3.2"/><path d="M4 14 C4 8 16 8 16 14 Z"/><circle cx="3.5" cy="5" r="2.4"/><circle cx="16.5" cy="5" r="2.4"/><path d="M0 13 C0 9 4 8.5 5 9.5 L3.5 13 Z M20 13 C20 9 16 8.5 15 9.5 L16.5 13 Z"/></svg>ABOUT</div>
      <div class="utility-link">
        <svg width="16" height="16" viewBox="0 0 16 16" fill="none" stroke="#c9d2e3" stroke-width="1.6"><rect x="1" y="2.5" width="14" height="12.5"/><line x1="1" y1="6" x2="15" y2="6"/><line x1="4.5" y1="0.5" x2="4.5" y2="4"/><line x1="11.5" y1="0.5" x2="11.5" y2="4"/></svg>EVENTS</div>
      <div class="utility-link">
        <svg width="15" height="15" viewBox="0 0 15 15"><circle cx="7.5" cy="7.5" r="5.5" fill="#c9d2e3" stroke="#c9d2e3" stroke-width="3" stroke-dasharray="2.2 2.1"/><circle cx="7.5" cy="7.5" r="2" fill="#25355a"/></svg>ACCOUNT</div>
      <div class="utility-link">
        <svg width="14" height="14" viewBox="0 0 14 14" fill="#c9d2e3"><path d="M3 0 L5.5 3.5 L4 5.5 C5 7.5 6.5 9 8.5 10 L10.5 8.5 L14 11 L12 14 C6 13 1 8 0 2 Z"/></svg>CONTACT</div>
    </nav>
  </header>

  <div class="category-bar">
    <nav class="categories">
      <span>Red Wine</span><span>White Wine</span><span>Sparkling</span><span>Rosé</span><span>Stickies</span><span>Imported</span><span>Wine Club</span>
    </nav>
    <div class="cart">
      <svg width="24" height="19" viewBox="0 0 24 19" fill="#ffffff"><path d="M0 0 H4 L5 3 H23 L20.5 11 H7.5 L8.2 13 H20 V15 H6.8 L2.8 2 H0 Z"/><circle cx="8.5" cy="17" r="1.8"/><circle cx="18" cy="17" r="1.8"/></svg>
      Shopping cart is empty
    </div>
  </div>

  <main class="content"></main>

  <article class="feature feature-education" style="left:110px">
    <div class="feature-photo" role="img" aria-label="Vineyard at sunset with a bunch of red grapes on the vine"></div>
    <svg class="corner-ribbon" width="145" height="140" viewBox="0 0 145 140"><polygon points="112,2 132,2 124,20" fill="#7d2a2c"/><polygon points="3,131 3,82 90,2 128,2" fill="#b3474a"/></svg>
    <div class="corner-label">EDUCATION</div>
    <div class="title-banner">
      <svg width="222" height="44" viewBox="0 0 222 44"><polygon points="204,34 222,34 222,44" fill="#7d2a2c"/><polygon points="0,17 18,0 222,0 222,34 18,34" fill="#b3474a"/></svg>
      <span>WINE COURSES</span>
    </div>
    <div class="read-more">READ MORE</div>
  </article>

  <article class="feature feature-club" style="left:440px">
    <div class="feature-photo" role="img" aria-label="Shopkeeper standing in the doorway of a wine store"></div>
    <svg class="corner-ribbon" width="145" height="140" viewBox="0 0 145 140"><polygon points="112,2 132,2 124,20" fill="#1f5fa8"/><polygon points="3,131 3,82 90,2 128,2" fill="#1e2a44"/></svg>
    <div class="corner-label">WINE CLUB</div>
    <div class="title-banner">
      <svg width="222" height="44" viewBox="0 0 222 44"><polygon points="204,34 222,34 222,44" fill="#1f5fa8"/><polygon points="0,17 18,0 222,0 222,34 18,34" fill="#1e2a44"/></svg>
      <span>LET US CHOOSE</span>
    </div>
    <div class="read-more">READ MORE</div>
  </article>

  <article class="feature feature-packs" style="left:770px">
    <div class="feature-photo" role="img" aria-label="Glass of red wine, bottle, cherry tomatoes, cheese and bread above a terraced vineyard"></div>
    <svg class="corner-ribbon" width="145" height="140" viewBox="0 0 145 140"><polygon points="112,2 132,2 124,20" fill="#7d2a2c"/><polygon points="3,131 3,82 90,2 128,2" fill="#b3474a"/></svg>
    <div class="corner-label">PURCHASED</div>
    <div class="title-banner">
      <svg width="222" height="44" viewBox="0 0 222 44"><polygon points="204,34 222,34 222,44" fill="#7d2a2c"/><polygon points="0,17 18,0 222,0 222,34 18,34" fill="#b3474a"/></svg>
      <span>MIXED PACKS</span>
    </div>
    <div class="read-more">READ MORE</div>
  </article>

  <div class="product bottle" style="left:192px;width:63px" role="img" aria-label="Red wine bottle"></div>
  <div class="product bottle" style="left:433px;width:68px" role="img" aria-label="Red wine bottle"></div>
  <div class="product bottle" style="left:674px;width:70px" role="img" aria-label="Red wine bottle"></div>
  <div class="product" style="left:896px;width:112px;background:linear-gradient(90deg,#efe6dc,#e2d6c6 40%,#3a3a22 46%,#4a4a2c 54%,#e2d6c6 60%,#efe6dc)" role="img" aria-label="White wine bottle"></div>
</body>
</html>
```